High Tech Real Estate Startup needs a business card

We are developing an innovative real estate marketing product based around advanced search and virtual reality.

We talk to people, we need business cards.

Target Market(s)

The target market is technology professionals and realtors.

Contact Information for Business Card

The information to be included will include

Name
Title
Phone Number
E-mail Address
www.quelzo.com

It should use simple iconography for each one of those fields.

Font styles to use
Other font styles liked:
• Co, Jubilat, Avenir

Colors

Designer to choose colors to be used in the design.

Requirements
Must have
• Clean aesthetic,
• Good use of negative space.
• It should use our company logo, shown in the attached file. It is able to use the negative of that logo (coloured font and white background) and I have attached other acceptable accent colours in a swatch file.
Should not have
• Should not be too busy
• No extraneous text (slogans, tag lines etc)

```html
<!DOCTYPE html>
<html lang="en">
<head>
<meta charset="utf-8">
<title>Quelzo Business Card</title>
<link rel="stylesheet" href="https://fonts.googleapis.com/css2?family=Montserrat:wght@400;500;600;700&display=swap">
<style>
  :root {
    --teal: #12bcc0;
    --charcoal: #2c3038;
    --night: #242424;
    --paper: #f5f5f5;
    --ink: #1f1f1f;
    --shadow: #a8a8ab;
    --amber: #f9b859;
    --coral: #f27a58;
    --white: #ffffff;
    --edge: #2a2f4a;
  }
  * { margin: 0; padding: 0; box-sizing: border-box; }
  html, body { width: 1200px; height: 900px; overflow: hidden; background: var(--white); }
  body { position: relative; font-family: "Montserrat", sans-serif; }
  .abs { position: absolute; }

  .brand-block {
    left: 139px; top: 282px; width: 288px; height: 288px;
    background: var(--teal); color: var(--white);
    display: flex; align-items: center; justify-content: center;
    font-size: 48px; font-weight: 500; letter-spacing: 1px;
  }

  .card-shadow { background: var(--shadow); width: 577px; height: 330px; }
  .card { width: 577px; height: 330px; overflow: hidden; }

  .front { left: 578px; top: 95px; background: var(--night); }
  .front .top-bar { left: 0; top: 0; width: 100%; height: 26px; background: var(--charcoal); }
  .front .field { left: 0; top: 26px; width: 100%; height: 279px; background: var(--night); }
  .front .base-bar { left: 0; top: 305px; width: 100%; height: 25px; background: var(--teal); }
  .front .brand-mark {
    left: 239px; top: 112px; width: 97px; height: 97px;
    background: var(--teal); color: var(--white);
    display: flex; align-items: center; justify-content: center;
    font-size: 16px; font-weight: 600;
  }

  .back { left: 578px; top: 480px; background: var(--paper); border: 1px solid var(--edge); }
  .back .field { left: 0; top: 0; width: 100%; height: 100%; background: var(--paper); }
  .back .identity { left: 0; top: 30px; width: 100%; text-align: center; }
  .identity .person { color: var(--teal); font-size: 25px; font-weight: 700; line-height: 1.1; }
  .identity .job-title { color: var(--ink); font-size: 18px; font-weight: 400; margin-top: 2px; }

  .icon-band { left: 0; top: 108px; width: 100%; height: 92px; display: flex; }
  .icon-cell { flex: 1; display: flex; align-items: center; justify-content: center; background: var(--charcoal); }
  .icon-cell.accent { background: var(--teal); }
  .icon-cell svg { width: 72px; height: 72px; }

  .contact-row { left: 0; top: 228px; width: 100%; height: 48px; display: flex; }
  .contact-item {
    flex: 1; display: flex; align-items: center; justify-content: center;
    font-size: 17px; color: var(--ink);
  }
  .contact-item.web { font-weight: 700; }
  .contact-item + .contact-item { border-left: 2px solid #555; }

  .color-strip { left: 0; top: 303px; width: 100%; height: 27px; display: flex; }
  .color-strip span { flex: 1; }
  .color-strip .s1 { background: var(--teal); }
  .color-strip .s2 { background: var(--amber); }
  .color-strip .s3 { background: var(--coral); }
</style>
</head>
<body>
  <div class="abs brand-block">QUELZO</div>

  <div class="abs card-shadow" style="left:568px;top:108px;"></div>
  <section class="abs card front">
    <div class="abs top-bar"></div>
    <div class="abs field" role="img" aria-label="Faint grey network of connected points across a dark background"></div>
    <div class="abs base-bar"></div>
    <div class="abs brand-mark">QUELZO</div>
  </section>

  <div class="abs card-shadow" style="left:568px;top:492px;"></div>
  <section class="abs card back">
    <div class="abs field" role="img" aria-label="Very faint grey network of connected points on a light background"></div>
    <div class="abs identity">
      <div class="person">Name Surname</div>
      <div class="job-title">Company Job Title</div>
    </div>

    <div class="abs icon-band">
      <div class="icon-cell">
        <svg viewBox="0 0 72 72" aria-label="Website">
          <circle cx="36" cy="36" r="34" fill="none" stroke="#fff" stroke-width="3"/>
          <rect x="20" y="22" width="32" height="23" rx="2" fill="#fff"/>
          <rect x="23" y="25" width="26" height="17" fill="#2c3038"/>
          <path d="M32 45h8l2 5H30z" fill="#fff"/>
          <rect x="27" y="49" width="18" height="2.5" rx="1" fill="#fff"/>
        </svg>
      </div>
      <div class="icon-cell accent">
        <svg viewBox="0 0 72 72" aria-label="Phone">
          <circle cx="36" cy="36" r="34" fill="none" stroke="#fff" stroke-width="3"/>
          <path d="M26 20c2-1 4-1 5 1l3 6c1 2 0 3-1 4l-2 2c1 4 5 8 9 10l2-2c1-1 2-2 4-1l6 3c2 1 2 3 1 5l-2 3c-2 2-5 2-8 1-9-4-16-11-20-20-1-3-1-6 1-8z" fill="#fff"/>
        </svg>
      </div>
      <div class="icon-cell">
        <svg viewBox="0 0 72 72" aria-label="Email">
          <circle cx="36" cy="36" r="34" fill="none" stroke="#fff" stroke-width="3"/>
          <rect x="19" y="25" width="34" height="22" rx="2" fill="none" stroke="#fff" stroke-width="2.5"/>
          <path d="M20 26l16 12 16-12M20 46l12-10M52 46l-12-10" fill="none" stroke="#fff" stroke-width="2"/>
        </svg>
      </div>
    </div>

    <div class="abs contact-row">
      <div class="contact-item web">www.quelzo.com</div>
      <div class="contact-item">+381770001234</div>
      <div class="contact-item">name@quelzo.com</div>
    </div>

    <div class="abs color-strip"><span class="s1"></span><span class="s2"></span><span class="s3"></span></div>
  </section>
</body>
</html>
```